Social responsible Renewable Energy company

We at voltaQ are an independent power producer company founded in 2021 that handles large scale deployment of Renewable Energy and carbon neutral Energy as a service model. We offer turnkey solutions using solar panel systems and this could be incorporated in our business cards. You can also find our logo in the documents provided. Another key issue is that the business cards will be printed on recicled paper, not sure if this is a limitation in deciding the design. The recycled sign should also be added on the business card and stating that the paper used was recycled. Our website is www.myvoltaq.example. It should also be very professional, not too dreamy but still needs to capture your imagination. We are really excited to get your ideas !

Target Market(s)

Renewable Energy market

Contact Information for Business Card

The business card will be printed on recycled paper. Name of the company is voltaQ. Website is www.myvoltaq.example

Requirements
Nice to have
• Our motto: Powered by renewable, driven by people.

```html
<!DOCTYPE html>
<html lang="en">
<head>
<meta charset="utf-8">
<title>voltaQ business card</title>
<link href="https://fonts.googleapis.com/css2?family=Rubik:wght@300;400;600;700&display=swap" rel="stylesheet">
<style>
  :root {
    --backdrop: #a59d97;
    --paper: #e9e0cb;
    --navy: #1d4468;
    --bright-blue: #1b76c2;
    --paper-text: #1d4468;
    --band-text: #eef1f4;
  }
  * { margin: 0; padding: 0; box-sizing: border-box; }
  html, body { width: 1200px; height: 864px; overflow: hidden; }
  body {
    background: var(--backdrop);
    font-family: "Rubik", sans-serif;
    display: flex; align-items: center; justify-content: center;
  }
  .card {
    position: relative;
    width: 840px; height: 480px;
    background: var(--paper);
    overflow: hidden;
    box-shadow: 0 18px 40px rgba(0,0,0,0.25);
  }
  .card-bands { position: absolute; inset: 0; }
  .recycle-mark { position: absolute; left: 58px; top: 40px; width: 58px; height: 58px; }
  .holder-name {
    position: absolute; left: 60px; top: 138px;
    font-weight: 700; font-size: 30px; color: var(--paper-text);
  }
  .holder-role {
    position: absolute; left: 60px; top: 210px;
    font-weight: 300; font-size: 15px; letter-spacing: 0.5px;
    color: var(--band-text); text-transform: uppercase;
  }
  .contact-list {
    position: absolute; left: 60px; top: 250px;
    list-style: none; color: var(--band-text);
    font-size: 19px; font-weight: 400; line-height: 30px;
  }
  .contact-list li { display: flex; align-items: center; gap: 12px; }
  .contact-list svg { width: 16px; height: 16px; fill: var(--band-text); }
  .brand-name {
    position: absolute; right: 48px; top: 110px;
    font-weight: 600; font-size: 96px; letter-spacing: -1px;
    color: var(--paper-text); line-height: 1;
  }
  .company-address {
    position: absolute; left: 520px; top: 310px;
    color: var(--band-text); font-size: 18px; line-height: 28px; font-weight: 300;
  }
  .company-address strong { font-weight: 600; display: block; }
</style>
</head>
<body>
  <div class="card">
    <svg class="card-bands" viewBox="0 0 840 480" aria-hidden="true">
      <polygon points="430,238 840,238 840,264 472,264" fill="var(--bright-blue)"/>
      <polygon points="0,196 412,196 448,264 840,264 840,480 0,480" fill="var(--navy)"/>
    </svg>

    <svg class="recycle-mark" viewBox="0 0 60 60" aria-label="Recycled paper">
      <g fill="none" stroke="var(--navy)" stroke-width="7" stroke-linecap="round">
        <path d="M22 14 A20 20 0 0 1 48 24"/>
        <path d="M50 36 A20 20 0 0 1 26 50"/>
        <path d="M14 44 A20 20 0 0 1 12 22"/>
      </g>
      <g fill="var(--navy)">
        <polygon points="44,14 56,26 40,30"/>
        <polygon points="32,42 30,58 18,48"/>
        <polygon points="4,26 16,14 20,28"/>
      </g>
    </svg>

    <div class="holder-name">Daniel Marsh</div>
    <div class="holder-role">Director</div>

    <ul class="contact-list">
      <li>
        <svg viewBox="0 0 16 16"><path d="M3 1h3l1.5 4-2 1.2a9 9 0 0 0 4.3 4.3L11 8.5l4 1.5v3a2 2 0 0 1-2 2A12 12 0 0 1 1 3a2 2 0 0 1 2-2z"/></svg>
        (555) 010 2040
      </li>
      <li>
        <svg viewBox="0 0 16 16"><path d="M1 3h14v10H1z M1 3l7 6 7-6" /></svg>
        info@myvoltaq.example
      </li>
      <li>
        <svg viewBox="0 0 16 16"><circle cx="8" cy="8" r="7"/></svg>
        www.myvoltaq.example
      </li>
    </ul>

    <div class="brand-name">voltaQ</div>

    <div class="company-address">
      <strong>VoltaQ</strong>
      1420 Meridian Rd.<br>
      Brightwater, ZZ 40516
    </div>
  </div>
</body>
</html>
```